Business Card Design

Business Card for professional consulting firm working with large financial institutions.

Target Market(s)

Executive buyers

Industry/Entity Type

Banking

Contact Information for Business Card

Mild creativity wanted. Not boring, but do elaborate artwork.

Font styles to use
Serif
Sans Serif

Colors

Designer to choose colors to be used in the design.

Requirements
Must have
• Standard business card features - company name, individual name, telephone, website, email, locations.
Nice to have
• Two colors
Should not have
• too many colors, fancy printing, cartoons.

```html
<!DOCTYPE html>
<html lang="en">
<head>
<meta charset="utf-8">
<title>Northvane Advisory — Business Card</title>
<link href="https://fonts.googleapis.com/css2?family=Alegreya+Sans:wght@400;700&display=swap" rel="stylesheet">
<style>
  :root {
    --backdrop: #3a3a3b;
    --card: #262627;
    --card-emboss: #1d1d1e;
    --ink: #f2f2f2;
    --ink-soft: #d6d6d6;
    --band-light: #bdbdbd;
    --band-slate: #3c4447;
  }
  * { margin: 0; padding: 0; box-sizing: border-box; }
  html, body { width: 799px; height: 1200px; overflow: hidden; }
  body {
    background: var(--backdrop);
    font-family: "Alegreya Sans", sans-serif;
    color: var(--ink);
    position: relative;
  }
  .card {
    position: absolute;
    left: 80px;
    width: 640px;
    height: 366px;
    background: var(--card);
    border-radius: 4px;
    overflow: hidden;
  }
  .card--front { top: 120px; }
  .card--back { top: 700px; }

  .front-brand {
    position: absolute;
    inset: 0;
    display: flex;
    align-items: center;
    justify-content: center;
    gap: 14px;
    font-size: 46px;
    font-weight: 400;
    color: var(--card-emboss);
    letter-spacing: 0.5px;
  }
  .front-brand .mark {
    width: 18px; height: 18px;
    border-radius: 50%;
    background: var(--card-emboss);
  }

  .back-brand {
    position: absolute;
    left: 44px;
    top: 66px;
    display: flex;
    align-items: center;
    gap: 10px;
    font-size: 30px;
    font-weight: 400;
    color: var(--ink);
  }
  .back-brand .mark {
    width: 12px; height: 12px;
    border-radius: 50%;
    background: var(--ink);
  }

  .person {
    position: absolute;
    left: 372px;
    top: 96px;
  }
  .person-name { font-size: 26px; font-weight: 700; line-height: 1.1; }
  .person-title { font-size: 15px; color: var(--ink-soft); margin-top: 2px; }

  .contact {
    position: absolute;
    left: 372px;
    top: 160px;
    font-size: 16px;
    line-height: 1.3;
    color: var(--ink-soft);
    list-style: none;
  }
  .contact li { display: flex; align-items: center; gap: 10px; }
  .contact .address { display: block; padding-left: 24px; margin-bottom: 4px; }
  .contact svg { width: 14px; height: 14px; fill: var(--ink); flex: none; }

  .band-light {
    position: absolute;
    left: 0;
    top: 276px;
    width: 280px;
    height: 12px;
    background: var(--band-light);
  }
  .footer-tab {
    position: absolute;
    left: 268px;
    top: 276px;
    right: 0;
    bottom: 0;
    background: var(--band-slate);
    border-top-left-radius: 22px;
    display: flex;
    align-items: center;
    padding-left: 60px;
    font-size: 18px;
    color: var(--ink);
  }
</style>
</head>
<body>
  <section class="card card--front" aria-label="Card front">
    <div class="front-brand"><span class="mark"></span>Northvane Advisory</div>
  </section>

  <section class="card card--back" aria-label="Card back">
    <div class="back-brand"><span class="mark"></span>Northvane Advisory</div>

    <div class="person">
      <p class="person-name">John Doe Smith</p>
      <p class="person-title">Managing Director</p>
    </div>

    <ul class="contact">
      <li class="address">234 Anywhere St., Any City,<br>Any Town, US 123456</li>
      <li>
        <svg viewBox="0 0 24 24" aria-hidden="true"><path d="M6.6 10.8a15.1 15.1 0 0 0 6.6 6.6l2.2-2.2a1 1 0 0 1 1-.25 11.4 11.4 0 0 0 3.6.57 1 1 0 0 1 1 1V20a1 1 0 0 1-1 1A17 17 0 0 1 3 4a1 1 0 0 1 1-1h3.5a1 1 0 0 1 1 1c0 1.250.2 2.46.57 3.6a1 1 0 0 1-.25 1z"/></svg>
        555.555.5555
      </li>
      <li>
        <svg viewBox="0 0 24 24" aria-hidden="true"><path d="M2 5h20v14H2z M3.5 6.5 12 13l8.5-6.5" stroke="#262627" stroke-width="1.6" fill="#f2f2f2"/></svg>
        johndoe@example.com
      </li>
    </ul>

    <div class="band-light"></div>
    <div class="footer-tab">www.yourwebsite.com</div>
  </section>
</body>
</html>
```